BriskLoom Wordpress Website

We require a WordPress website that emulates the sleek design and functionality of https://www.tulvorix.example and https://quenlap.example/. The site should showcase our AI-powered customer support solutions with a modern, professional aesthetic.
Homepage
The homepage should feature a bold headline highlighting our AI capabilities, followed by concise sections outlining our key offerings:
AI-powered customer support
Data integration and deployment
Knowledge system integration
AI help desks and chat agents
Customer feedback insights
Include eye-catching visuals or animations to illustrate these concepts.
Navigation
The main navigation menu should include:
Product
Platform
Company
News
Learn More
Key Pages
Product Page: Detail our AI solutions, their benefits, and use cases.
Platform Page: Explain our technology, integration capabilities, and deployment process.
Company Page: Share our mission, team, and values.
News Page: Feature latest updates, press releases, and blog posts.
Call-to-Action
Implement a prominent "Learn More" button that directs users to an enrollment page. Our team will manage inquiries from this point.
Footer
Include a "Contact Us" section in the footer for easy access to our contact information.
Design Elements
Use a clean, minimalist design with ample white space
Incorporate a color scheme that reflects trust and innovation
Utilize smooth scrolling and subtle animations for enhanced user experience
Ensure mobile responsiveness for all devices
Technical Requirements
Build on WordPress for easy content management
Optimize for fast loading speeds and SEO
The website should convey our expertise in AI-driven customer support solutions while providing an intuitive user experience that guides visitors toward learning more about our services
Industry/Entity Type
AI Chat Agents

```html
<!DOCTYPE html>
<html lang="en">
<head>
<meta charset="utf-8">
<title>BriskLoom — AI Customer Support</title>
<link href="https://fonts.googleapis.com/css2?family=Poppins:wght@300;400;500;600;700;800&display=swap" rel="stylesheet">
<style>
:root{
  --teal:#3f8f91;
  --teal-mid:#4a9597;
  --teal-dark:#2a5e62;
  --teal-deep:#1f4b4f;
  --teal-pale:#eef4f4;
  --teal-soft:#d7ebeb;
  --ink:#2b2b2b;
  --muted:#555;
  --white:#fff;
}
*{margin:0;padding:0;box-sizing:border-box}
html,body{width:1200px;height:3145px;overflow:hidden}
body{font-family:'Poppins',sans-serif;color:var(--ink);background:var(--white);position:relative}
.abs{position:absolute}
.brand{display:flex;align-items:center;gap:8px;font-weight:500;font-size:27px;color:var(--teal-dark)}
.brand-dot{width:38px;height:38px;border-radius:50%;background:var(--teal-dark)}
.pill{display:flex;align-items:center;justify-content:space-between;border-radius:24px;font-weight:500;font-size:12px;padding:0 6px 0 18px}
.pill-dot{width:26px;height:26px;border-radius:50%;background:var(--teal-dark)}

/* header */
.site-header{left:0;top:0;width:1200px;height:59px}
.site-header .brand{position:absolute;left:122px;top:6px}
.main-nav a{position:absolute;top:20px;font-size:12px;font-weight:500;color:var(--ink);text-decoration:none}
.header-cta{left:952px;top:12px;width:125px;height:34px;border:1.5px solid var(--teal-dark);color:var(--ink)}

/* hero */
.hero{left:0;top:59px;width:1200px;height:606px;border-bottom-right-radius:90px;border-bottom:6px solid var(--teal);overflow:hidden;
  background:linear-gradient(100deg,#142a2c 0%,#23494c 35%,#2f6a6c 60%,#1d3d40 100%)}
.hero-photo{position:absolute;inset:0;background:radial-gradient(ellipse at 40% 30%,rgba(120,170,165,.35),transparent 55%),radial-gradient(ellipse at 80% 40%,rgba(80,200,200,.25),transparent 50%)}
.hero-title{left:120px;top:360px;font-size:70px;font-weight:800;color:var(--white);letter-spacing:-1px}
.hero-text{left:123px;top:455px;font-size:11.5px;line-height:18px;color:var(--white);font-weight:500}
.hero-tag{left:123px;top:514px;font-size:11.5px;font-weight:600;color:var(--white)}
.hero-badge{left:283px;top:505px;width:35px;height:35px;border-radius:50%;background:var(--white);border:2px solid var(--teal)}
.hero-cta{left:333px;top:504px;width:127px;height:35px;background:var(--white);color:var(--teal-dark)}

.section-title{position:absolute;left:0;width:1200px;text-align:center;font-size:34px;font-weight:700;color:var(--ink)}
.swoosh{position:absolute}

/* feature cards */
.feature{top:794px;width:306px;height:242px;background:var(--teal-pale);border-radius:10px;border-bottom:4px solid var(--teal);padding:0 26px}
.feature-icon{position:absolute;left:26px;top:40px;width:74px;height:74px;border-radius:50%;background:var(--teal-dark)}
.feature h3{position:absolute;left:26px;top:130px;font-size:22px;font-weight:500}
.feature p{position:absolute;left:26px;top:163px;width:240px;font-size:15px;line-height:22px;color:var(--muted)}

/* conversational */
.robot{left:180px;top:1155px;width:350px;height:385px;border-radius:50%;background:radial-gradient(circle at 55% 40%,#b9c7c8,#5e7275 60%,#2c3d40);border:14px solid var(--teal)}
.point{left:617px;width:470px}
.point h4{font-size:15px;font-weight:500;color:var(--ink);padding-left:37px;position:relative;line-height:19px}
.point p{font-size:11.5px;color:var(--muted);padding-left:37px;line-height:22px}
.tick{position:absolute;left:12px;top:3px;width:14px;height:14px;border-radius:50%;background:var(--teal)}
.point-hi{background:var(--teal-soft);border-radius:8px;padding:6px 0}

/* contact */
.contact-box{left:218px;top:1593px;width:764px;height:203px;border-radius:10px;background:linear-gradient(90deg,var(--teal-dark),var(--teal-mid))}
.contact-box h2{position:absolute;left:0;top:46px;width:100%;text-align:center;color:var(--white);font-size:34px;font-weight:700}
.contact-cta{left:318px;top:112px;width:127px;height:35px;background:var(--white)}

/* offerings */
.offerings{left:0;top:1859px;width:1200px;height:598px;background:var(--teal-mid);overflow:hidden}
.offerings .section-title{color:var(--white);top:44px}
.offer-core{left:500px;top:126px;width:205px;height:220px;border-radius:50%;background:var(--teal-dark)}
.offer{font-size:15px;font-weight:500;color:var(--white);line-height:18px}
.offer-icon{width:52px;height:52px;border-radius:50%;background:var(--white)}
.offer-icon::after{content:"";position:absolute;left:16px;top:16px;width:20px;height:20px;border-radius:50%;background:var(--teal-dark)}
.ghost-text{left:0;top:490px;width:1200px;text-align:center;font-size:114px;font-weight:800;color:rgba(255,255,255,.12);white-space:nowrap;letter-spacing:-2px}
.ring{border-radius:50%;border:26px solid rgba(255,255,255,.9)}

/* news */
.news-card{top:2572px;width:306px}
.news-img{width:306px;height:173px;border-radius:10px}
.news-date{position:absolute;top:186px;left:12px;font-size:9px;color:var(--teal);font-weight:600}
.news-title{position:absolute;top:202px;left:12px;font-size:14px;font-weight:600;line-height:17px;width:250px}
.news-arrow{position:absolute;right:0;top:220px;width:21px;height:21px;border-radius:50%;background:var(--teal)}
.news-rule{position:absolute;top:247px;left:0;width:306px;border-top:1px solid #ccc}
.news-cta{left:533px;top:2845px;width:134px;height:35px;background:var(--teal-dark);color:var(--white)}
.news-cta .pill-dot{background:var(--white)}

/* footer */
.site-footer{left:0;top:2925px;width:1200px;height:220px;background:var(--teal-dark);color:var(--white)}
.site-footer .brand{position:absolute;left:121px;top:36px;color:var(--white);font-size:24px}
.site-footer .brand-dot{background:var(--white);width:32px;height:32px}
.foot-about{left:120px;top:80px;width:210px;font-size:8.5px;line-height:15px}
.foot-col h5{font-size:19px;font-weight:600;margin-bottom:10px}
.foot-col li{list-style:none;font-size:9px;line-height:17.5px}
.foot-sep{top:38px;width:1px;height:160px;background:rgba(255,255,255,.3)}
.foot-item{display:flex;align-items:center;gap:10px;font-size:9px;margin-bottom:12px}
.foot-ico{width:21px;height:21px;border-radius:50%;background:var(--teal-mid)}
.foot-copy{left:120px;top:198px;width:956px;border-top:1px solid rgba(255,255,255,.3);text-align:center;font-size:8px;padding-top:8px}
</style>
</head>
<body>

<header class="abs site-header">
  <div class="brand"><span class="brand-dot"></span>BriskLoom</div>
  <nav class="main-nav">
    <a href="#" style="left:635px">Product</a>
    <a href="#" style="left:717px">Platform</a>
    <a href="#" style="left:803px">Company</a>
    <a href="#" style="left:898px">News</a>
  </nav>
  <a class="abs pill header-cta">Learn More <span class="pill-dot"></span></a>
</header>

<section class="abs hero">
  <div class="hero-photo" role="img" aria-label="Photo of a support agent beside a desktop monitor in a teal-lit office"></div>
  <h1 class="abs hero-title">Meet BriskLoom</h1>
  <svg class="abs" style="left:330px;top:433px" width="300" height="24" viewBox="0 0 300 24"><path d="M4 18 Q150 4 296 10" stroke="#fff" stroke-width="5" fill="none" stroke-linecap="round"/></svg>
  <p class="abs hero-text">Elevate your users' experience, a new type of conversation awaits.<br>Enhance your customer experience with BriskLoom's AI Assistant.</p>
  <p class="abs hero-tag">Always ready, always on -</p>
  <span class="abs hero-badge"></span>
  <a class="abs pill hero-cta">Get Started <span class="pill-dot"></span></a>
</section>

<h2 class="section-title" style="top:714px">Revolutionize your Customer Interactions:</h2>
<svg class="swoosh" style="left:566px;top:752px" width="172" height="18"><path d="M3 14 Q86 2 169 8" stroke="#3f8f91" stroke-width="4" fill="none" stroke-linecap="round"/></svg>

<article class="abs feature" style="left:122px"><span class="feature-icon"></span><h3>Get Answers</h3><p>Users will find the information they need in seconds.</p></article>
<article class="abs feature" style="left:447px"><span class="feature-icon"></span><h3>Solve Problems</h3><p>Concerns will be Addressed quickly with expert assistance</p></article>
<article class="abs feature" style="left:773px"><span class="feature-icon"></span><h3>Take Action</h3><p>Users will activate services and features immediately</p></article>

<h2 class="section-title" style="top:1085px">All through Natural, Conversational Experiences.</h2>
<svg class="swoosh" style="left:797px;top:1123px" width="222" height="18"><path d="M3 14 Q110 2 219 8" stroke="#3f8f91" stroke-width="4" fill="none" stroke-linecap="round"/></svg>

<div class="abs robot" role="img" aria-label="Illustration of an AI robot head in profile"></div>

<div class="abs point" style="top:1168px">
  <h4><span class="tick"></span>BriskLoom Enables you to:</h4>
  <p>Engage and delight customers with an AI agent aligned to your brand<br>Provide real-time support for a wide variety of uses from simple to complex</p>
</div>
<div class="abs point point-hi" style="top:1247px;width:466px">
  <h4>Make AI your own with BriskLoom's<br>Conversational Platform:</h4>
  <p>Ground your BriskLoom AI agent in your company's identity &amp; knowledge<br>Solve problems quickly and effectively</p>
</div>
<div class="abs point" style="top:1358px">
  <h4><span class="tick"></span>BriskLoom prioritizes trust and security:</h4>
  <p>Built-in supervision and auditing<br>Secure integrations<br>Strong data governance and privacy<br>Discover how BriskLoom can transform your customer experience with customized<br>conversational AI.</p>
</div>

<section class="abs contact-box">
  <h2>Contact us today</h2>
  <svg class="abs" style="left:290px;top:86px" width="182" height="16"><path d="M3 12 Q90 2 179 6" stroke="#fff" stroke-width="4" fill="none" stroke-linecap="round"/></svg>
  <a class="abs pill contact-cta">Learn More <span class="pill-dot"></span></a>
</section>

<section class="abs offerings">
  <div class="abs ring" style="left:8px;top:20px;width:210px;height:210px"></div>
  <h2 class="section-title">Our key Offerings:</h2>
  <svg class="abs" style="left:594px;top:84px" width="162" height="16"><path d="M3 12 Q80 2 159 6" stroke="#fff" stroke-width="4" fill="none" stroke-linecap="round"/></svg>
  <svg class="abs" style="left:0;top:0" width="1200" height="480">
    <g stroke="rgba(255,255,255,.5)" stroke-width="1" fill="none">
      <path d="M418 166 H496"/><path d="M697 166 H775"/><path d="M445 305 H500"/><path d="M697 305 H752"/><path d="M600 346 V378"/>
    </g>
    <g fill="#2a5e62"><circle cx="496" cy="166" r="3"/><circle cx="697" cy="166" r="3"/><circle cx="500" cy="305" r="3"/><circle cx="697" cy="305" r="3"/><circle cx="600" cy="346" r="3"/></g>
  </svg>
  <div class="abs offer-core"></div>
  <div class="abs offer" style="left:200px;top:148px;text-align:right;width:153px">AI-powered<br>Customer Support</div>
  <div class="abs offer-icon" style="left:366px;top:140px"></div>
  <div class="abs offer-icon" style="left:774px;top:140px"></div>
  <div class="abs offer" style="left:841px;top:148px">Knowledge<br>System Integration</div>
  <div class="abs offer" style="left:200px;top:287px;text-align:right;width:180px">Customer<br>Feedback Insights</div>
  <div class="abs offer-icon" style="left:392px;top:279px"></div>
  <div class="abs offer-icon" style="left:752px;top:279px"></div>
  <div class="abs offer" style="left:820px;top:287px">AI help Desks<br>and Chat Agents</div>
  <div class="abs offer-icon" style="left:574px;top:380px"></div>
  <div class="abs offer" style="left:0;top:446px;width:1226px;text-align:center">Data integration and deployment</div>
  <div class="abs ghost-text">OUR KEY OFFERINGS</div>
</section>

<h2 class="section-title" style="top:2502px">Latest News</h2>
<svg class="swoosh" style="left:606px;top:2540px" width="96" height="14"><path d="M3 10 Q48 2 93 5" stroke="#3f8f91" stroke-width="4" fill="none" stroke-linecap="round"/></svg>

<article class="abs news-card" style="left:122px">
  <div class="news-img" role="img" aria-label="Photo of a small robot at a desk beside a laptop" style="background:linear-gradient(135deg,#d8d4cc,#8d8a83)"></div>
  <span class="news-date">August 20, 2024</span>
  <h3 class="news-title">Lorem ipsum dolor sit amet, consectetur adipiscing elit.</h3>
  <span class="news-arrow"></span><span class="news-rule"></span>
</article>
<article class="abs news-card" style="left:447px">
  <div class="news-img" role="img" aria-label="Photo of hands typing on a laptop with floating CRM icons" style="background:linear-gradient(135deg,#b9b9b9,#4f4f4f)"></div>
  <span class="news-date">August 20, 2024</span>
  <h3 class="news-title">Lorem ipsum dolor sit amet, consectetur adipiscing elit.</h3>
  <span class="news-arrow"></span><span class="news-rule"></span>
</article>
<article class="abs news-card" style="left:773px">
  <div class="news-img" role="img" aria-label="Photo of a woman working at a laptop with glowing screens" style="background:linear-gradient(135deg,#2a2238,#6a4f5c)"></div>
  <span class="news-date">August 20, 2024</span>
  <h3 class="news-title">Lorem ipsum dolor sit amet, consectetur adipiscing elit.</h3>
  <span class="news-arrow"></span><span class="news-rule"></span>
</article>

<a class="abs pill news-cta">View All News <span class="pill-dot"></span></a>

<footer class="abs site-footer">
  <div class="brand"><span class="brand-dot"></span>BriskLoom</div>
  <p class="abs foot-about">Lorem ipsum dolor sit amet, consectetur adipiscing elit. Duis venenatis, eros at ultricies consectetur, leo dui condimentum nisl, non tempor libero eros ut nunc.</p>
  <span class="abs foot-sep" style="left:374px"></span>
  <div class="abs foot-col" style="left:450px;top:32px"><h5>Quick Links</h5><ul><li>Product</li><li>Platform</li><li>Company</li><li>News</li><li>Learn More</li></ul></div>
  <span class="abs foot-sep" style="left:635px"></span>
  <div class="abs foot-col" style="left:700px;top:32px"><h5>Contact Us</h5>
    <div class="foot-item"><span class="foot-ico"></span>555-017-2048</div>
    <div class="foot-item"><span class="foot-ico"></span>hello@briskloom.example</div>
  </div>
  <span class="abs foot-sep" style="left:894px"></span>
  <div class="abs foot-col" style="left:990px;top:32px"><h5>Follow Us</h5>
    <div class="foot-item"><span class="foot-ico"></span>Friendlane</div>
    <div class="foot-item"><span class="foot-ico"></span>Linkfolio</div>
    <div class="foot-item"><span class="foot-ico"></span>Chirpline</div>
  </div>
  <p class="abs foot-copy">© 2024 by BriskLoom. All Rights Reserved</p>
</footer>

</body>
</html>
```